Taking a Paper and turning into a wonderful White Paper for Prospects and Clients

This is a white paper I need designed. I am including my company brochure so you can see the design/fonts being used and I'm including a white paper created - one that I like very much.

I am "NOT" looking for a cookie cutter white paper. I'm looking for a nice, clean design but with some creativity. Check out the white paper I included and you will get the idea.

Also included:
- the paper to be designed
- the paper to be designed "WITH" suggested design features such as carve outs, call outs and such

A few things I "DO NOT" like:
- images that are cheesy or corny
* people sitting at a table in a meeting
* Buildings

The white paper I included did not use pictures but had more design created by the firm. I like this approach and will probably give something like this more weight but is not required.

Reason: Realized time frame was too tight

Target Market(s)

Higher-End, wealthier clients

Industry/Entity Type

It Company

Requirements
Must have
• I DO NOT want the copy to be bunched together. The layout should flow where the copy is broken in the right spots to make reading easier. If you read a paper and it is just copy, interest is lost by everyone.
• COLORS: you can see from what I have included the colors I use
• My preference are very balanced colors using "clean spacing"

```html
<!DOCTYPE html>
<html lang="en">
<head>
<meta charset="utf-8">
<title>Verance White Paper – Acting in Your Best Interest</title>
<link rel="stylesheet" href="https://fonts.googleapis.com/css2?family=Cabin:wght@600;700&family=Nunito+Sans:ital,wght@0,300;0,400;1,300;1,700&family=PT+Serif:wght@700&family=Tenor+Sans&display=swap">
<style>
  :root {
    --ink-teal: #1c4250;
    --band-light: #3d6e76;
    --band-dark: #18394380;
    --band-deep: #183a44;
    --body-grey: #5a5f63;
    --figure-grey: #a9abad;
    --page-white: #ffffff;
    --backdrop: #ffffff;
    --heading: "Cabin", sans-serif;
    --body: "Nunito Sans", sans-serif;
    --display: "Tenor Sans", sans-serif;
    --quote: "PT Serif", serif;
  }
  * { box-sizing: border-box; margin: 0; padding: 0; }
  html, body { width: 1200px; height: 520px; overflow: hidden; background: var(--backdrop); }
  .spread { position: relative; width: 1200px; height: 520px; }
  .page {
    position: absolute; top: 14px; width: 368px; height: 476px;
    background: var(--page-white);
    box-shadow: 3px 5px 9px rgba(0,0,0,0.28);
    font-family: var(--body); color: var(--body-grey);
    overflow: hidden;
  }
  .page--intro { left: 26px; }
  .page--story { left: 416px; }
  .page--verdict { left: 808px; }
  .wordmark {
    position: absolute; left: 24px; top: 22px;
    font-family: var(--heading); font-weight: 700; font-size: 6px;
    letter-spacing: 0.8px; color: var(--ink-teal);
  }
  .wordmark--faint { color: rgba(255,255,255,0.25); }
  .body-copy { font-size: 6.6px; line-height: 10.5px; font-weight: 300; }
  .block { position: absolute; }

  /* intro page */
  .callout {
    position: absolute; left: 80px; width: 240px;
    font-family: var(--heading); font-weight: 700; font-size: 13.2px; line-height: 15.5px;
    color: var(--ink-teal); padding-left: 24px;
  }
  .callout::before {
    content: "›"; position: absolute; left: 0; top: 6px;
    font-size: 14px; line-height: 14px;
  }
  .duty-list {
    position: absolute; left: 90px; top: 256px; list-style: none;
    font-weight: 700; font-style: italic; font-size: 8px; line-height: 14px;
    color: var(--ink-teal); letter-spacing: -0.2px;
  }

  /* story page */
  .story-band {
    position: absolute; left: 0; top: 0; width: 100%; height: 132px;
    background: radial-gradient(ellipse at 50% 45%, var(--band-light) 0%, var(--band-deep) 85%);
  }
  .story-lede {
    position: absolute; left: 52px; top: 46px; width: 282px;
    font-family: var(--display); font-size: 11.6px; line-height: 15px; color: #f2f5f5;
  }
  .story-flow {
    position: absolute; left: 28px; top: 158px; width: 312px;
    font-style: italic;
  }
  .story-flow p { margin-bottom: 10px; }
  .advisor-figure {
    float: left; width: 130px; height: 108px; margin: 2px 10px 4px 0;
    background: linear-gradient(160deg, #c4c6c8 0%, var(--figure-grey) 60%, #7e8589 100%);
  }
  .story-heading {
    font-family: var(--heading); font-weight: 700; font-style: normal;
    font-size: 12px; line-height: 14px; color: var(--ink-teal);
    text-align: right; margin: 12px 4px 16px 0;
  }

  /* verdict page */
  .fact-intro { left: 50px; top: 60px; width: 290px; font-style: italic; }
  .fact-heading {
    position: absolute; left: 130px; top: 92px;
    font-family: var(--heading); font-weight: 700; font-size: 13.6px; color: var(--ink-teal);
  }
  .fact-body { left: 50px; top: 128px; width: 292px; font-style: italic; text-indent: 28px; }
  .question-box {
    position: absolute; left: 50px; top: 206px; width: 184px; height: 91px;
    background: radial-gradient(ellipse at 50% 40%, var(--band-light) 0%, var(--band-deep) 90%);
    font-family: var(--display); font-size: 25px; line-height: 27px; color: #ffffff;
    padding: 12px 0 0 22px;
  }
  .tells-you {
    position: absolute; left: 84px; top: 314px;
    font-family: var(--display); font-size: 10.5px; color: #3c4347;
  }
  .answer-quote {
    position: absolute; left: 92px; top: 336px;
    font-family: var(--quote); font-weight: 700; font-size: 19.5px; color: var(--ink-teal);
  }
  .closing { left: 50px; top: 376px; width: 284px; font-weight: 400; }
</style>
</head>
<body>
<main class="spread">

  <section class="page page--intro">
    <div class="wordmark">VERANCE</div>
    <p class="block body-copy" style="left:50px; top:86px; width:280px;">Here at Verance – where we audit advisers for our clients covering areas such as fees charged, performance delivered, and investments used – we make certain our clients have great advisers.</p>
    <p class="block body-copy" style="left:50px; top:144px; width:280px;">But, our paramount demand, made of all the advisers we audit is</p>
    <p class="callout" style="top:164px;">the Financial Advisor “Acts in our client’s best interest”</p>
    <p class="block body-copy" style="left:50px; top:212px; width:285px;">When, working on your behalf, we audit the Registered Investment Advisors, Wealth Managers, Private Bankers, Trust Officers, Brokers or whatever other titles the financial professional may have, what concerns us is that they:</p>
    <ul class="duty-list">
      <li>- be honest with you</li>
      <li>- provide you with sound advice</li>
      <li>- look out for your best interest</li>
      <li>- offer advice for a fair fee, “or” fair compensation;</li>
    </ul>
    <p class="block body-copy" style="left:50px; top:320px;">and then, above all;</p>
    <p class="callout" style="top:348px;">we must be able to verify that your advisors are consistently doing the right things for you.</p>
  </section>

  <section class="page page--story">
    <div class="story-band"></div>
    <div class="wordmark wordmark--faint">VERANCE</div>
    <p class="story-lede">Let us now tell you a cautionary tale. This story illustrates some eventual pitfalls of choosing financial advisors based solely on whether they work under the fiduciary standard.</p>
    <div class="story-flow body-copy">
      <p style="padding-left:22px;">Three sports stars – Premier Baseball League pitchers Ray Oldham and Jack Pelley, and National Gridiron League quarterback Mark Salazar – believed they were bringing their “A-game” to the search for a great, trustworthy financial advisor.</p>
      <div class="advisor-figure" role="img" aria-label="Illustration of grey figures handing over a money bag to a financial advisor"></div>
      <h2 class="story-heading">Arun Natesan, the financial advisor they chose, seemed to be made of all the right stuff.</h2>
      <p>He worked for the Harbor City-based KVL Wealth Advisors. According to his business bios and cards, he was a Certified Public Account. The Gridiron Players Guild had endorsed him. Furthermore, he regularly attended the same church as Salazar and had an interest in charity work.</p>
      <p>Arun Natesan, nonetheless, turned out to be ruinously unscrupulous. He was not, in fact, a CPA. By fraudulent means, he transferred money out of his clients’ accounts, often without their consent, into The Seat Exchange, a financially-distressed company. And as a Seat Exchange board member, Natesan had multiple, egregious conflicts of interest that he never disclosed to his clients. By the time the deceitful scheme was uncovered and stopped, Natesan had misdirected $33 million of the three athletes’ money and nearly all of it was lost.</p>
    </div>
  </section>

  <section class="page page--verdict">
    <div class="wordmark">VERANCE</div>
    <p class="block body-copy fact-intro">One crucial fact got left out of most of the reporting on that story, namely, that</p>
    <h2 class="fact-heading">Arun Natesan was a fiduciary.</h2>
    <p class="block body-copy fact-body">As a Registered Investment Advisor working through KVL Capital Management, Natesan was legally required to put his clients’ interests before his own and to act in their best interests. He failed to do that. Subsequently, the National Securities Board’s federal case against him was settled without his clients being fully reimbursed.</p>
    <div class="question-box">Was this avoidable?</div>
    <p class="tells-you">Verance tells you</p>
    <p class="answer-quote">“Yes, this was avoidable.”</p>
    <p class="block body-copy closing">What happened to Mark Salazar does not have to happen to you. Verance pro-actively verifies that your financial advisors are consistently acting in your best interest.</p>
  </section>

</main>
</body>
</html>
```